Corvane Project Services - Flyer

Project Breif:
I need a single page A4 Capability Statement, which will be used to market our services to prospective clients, both in print and via email PDF.
It needs to look professional and should incorporate the elements I have uploaded into files, these include:
Capability Statement Text
Corvane Services Company Logo
Additional Logo’s (Tools We Use)
Glimmer Bay Pics can be cut into the page
I have included examples of capability statements as a guide to what i am looking for.
Regards
Derek
Engineering Consulting

```html
<!DOCTYPE html>
<html lang="en">
<head>
<meta charset="utf-8">
<title>Corvane Project Services – Capability Statement</title>
<link href="https://fonts.googleapis.com/css2?family=Montserrat:wght@400;500;600;700&display=swap" rel="stylesheet">
<style>
  :root{
    --navy:#1b2f7a;
    --navy-deep:#15246a;
    --blue:#1f6fc2;
    --blue-bright:#1a8ad8;
    --sky:#7cc2ee;
    --heading:#1d4f9e;
    --text:#3a3f4a;
    --item:#2f3440;
    --white:#ffffff;
    --photo-a:#eef2f7;
    --photo-b:#c9d6e6;
  }
  *{box-sizing:border-box;margin:0;padding:0}
  html,body{width:849px;height:1200px;overflow:hidden;background:#fff}
  body{font-family:"Montserrat",sans-serif;color:var(--text)}
  .flyer{position:relative;width:849px;height:1200px;background:linear-gradient(#fff 0%,#fff 70%,#f3f4f6 100%);overflow:hidden}
  .hero{position:absolute;left:0;top:0}
  .brand{position:absolute;left:30px;top:36px;width:230px;text-align:center;color:var(--white)}
  .brand-mark{width:72px;height:72px;border-radius:50%;background:var(--white);opacity:.9;margin:0 auto 24px}
  .brand-name{font-size:17px;font-weight:600;letter-spacing:1.5px;line-height:1.2}
  .brand-name span{display:block;font-size:12px;letter-spacing:8px;margin-top:3px}
  .intro{position:absolute;left:31px;top:454px;width:386px}
  .intro h2{font-size:13px;font-weight:700;color:var(--heading);margin-bottom:10px}
  .intro p{font-size:12.6px;line-height:15.4px;text-align:justify;margin-bottom:10px}
  .intro section{margin-bottom:6px}
  .intro .expertise h2{margin-bottom:4px}
  .intro .expertise p{margin-bottom:4px}
  .services{position:absolute;left:478px;top:448px;width:340px}
  .services-title{font-size:22px;font-weight:700;color:var(--heading);letter-spacing:.3px;margin-bottom:14px}
  .services-title span{color:#5a8fd0}
  .tag{position:relative;display:block;width:212px;height:24px;background:linear-gradient(90deg,var(--blue),var(--blue-bright));color:var(--white);font-size:14px;font-weight:700;line-height:24px;padding-left:8px}
  .tag svg{position:absolute;right:-16px;top:0}
  .list{list-style:none;margin:12px 0 0}
  .list li{font-size:13px;color:var(--item);height:23.2px;line-height:23.2px;padding-left:21px;position:relative}
  .list li::before{content:"→";position:absolute;left:0;top:0;font-size:12px}
  .group{position:absolute;left:0;width:340px}
  .footer{position:absolute;left:0;top:1062px}
  .contact{position:absolute;left:31px;top:1103px;color:var(--white);font-size:12.5px;letter-spacing:1.3px;font-weight:500}
  .contact li{list-style:none;display:flex;align-items:center;height:20px;margin-bottom:1px}
  .contact b{font-weight:700}
  .contact svg{margin-right:10px}
  .foot-mark{position:absolute;left:760px;top:1098px;width:54px;height:54px;border-radius:50%;background:var(--white);opacity:.9}
</style>
</head>
<body>
<div class="flyer">

  <svg class="hero" width="849" height="430" viewBox="0 0 849 430">
    <defs>
      <linearGradient id="navyGrad" x1="0" y1="0" x2="1" y2="1">
        <stop offset="0" stop-color="#15246a"/>
        <stop offset=".6" stop-color="#1f3f95"/>
        <stop offset="1" stop-color="#2a63b8"/>
      </linearGradient>
      <linearGradient id="skyGrad" x1="0" y1="0" x2="1" y2="0">
        <stop offset="0" stop-color="#6fb8ea"/>
        <stop offset="1" stop-color="#2e73c4"/>
      </linearGradient>
      <linearGradient id="photoGrad" x1="0" y1="0" x2="1" y2="1">
        <stop offset="0" stop-color="#f4f6fa"/>
        <stop offset=".5" stop-color="#dde5ef"/>
        <stop offset="1" stop-color="#bccbe0"/>
      </linearGradient>
    </defs>
    <path d="M318,298 C420,190 480,70 540,0 L849,0 L849,410 C700,425 480,405 318,298 Z" fill="#1f6fc2"/>
    <path role="img" aria-label="Photo of hands reviewing project charts and reports at a desk" d="M320,292 C420,185 480,68 536,0 L849,0 L849,400 C700,418 480,398 320,292 Z" fill="url(#photoGrad)"/>
    <path d="M0,0 L560,0 C470,70 420,220 330,300 C250,370 120,410 0,425 Z" fill="url(#skyGrad)"/>
    <path d="M0,0 L548,0 C440,90 380,150 250,190 C160,215 80,205 0,200 Z" fill="url(#navyGrad)"/>
    <path d="M548,0 C440,90 380,150 250,190" fill="none" stroke="#9fd3f5" stroke-width="2" opacity=".7"/>
  </svg>

  <div class="brand">
    <div class="brand-mark"></div>
    <div class="brand-name">CORVANE PROJECT<span>SERVICES</span></div>
  </div>

  <div class="intro">
    <section>
      <h2>About Us:</h2>
      <p>Our goal is to make successful project delivery more achievable and repeatable.</p>
      <p>We are continually innovating, evolving and learning, utilizing the latest industry tools and techniques to deliver real value to our clients.</p>
      <p>We are passionate about empowering organisations to achieve their objectives, on time and on budget.</p>
    </section>
    <section>
      <h2>Our Team</h2>
      <p>Our goal is to make successful project delivery more achievable and repeatable.</p>
      <p>We are continually innovating, evolving and learning, utilizing the latest industry tools and techniques to deliver real value to our clients.</p>
      <p>We are passionate about empowering organisations to achieve their objectives, on time and on budget.</p>
    </section>
    <section class="expertise">
      <h2>Our Expertise</h2>
      <p>For over 20 years we have been helping our clients to successfully deliver capital projects within the pharmaceutical and biotechnology sectors.</p>
      <p>During this time, we have worked closely with multinational healthcare companies and leading A&amp;E firms, on a variety of business-critical projects.</p>
      <p>Our experience and knowledge of project control gives our client’s unparalleled visibility of Cost, Schedule and Risk through the lifecycle of their projects.</p>
      <p>This visibility allows our clients to make timely informed decisions which increase efficiency and project performance.</p>
    </section>
  </div>

  <div class="services">
    <h2 class="services-title"><span>CORE</span> SERVICES:</h2>

    <div class="group" style="top:44px">
      <span class="tag">Planning and Scheduling<svg width="18" height="24" viewBox="0 0 18 24"><path d="M0,0 L8,0 L16,12 L8,24 L0,24 L8,12 Z" fill="#1a8ad8"/></svg></span>
      <ul class="list">
        <li>Tender Planning</li>
        <li>Interactive Planning / Pull Planning</li>
        <li>CPM Planning &amp; Scheduling</li>
        <li>Agile / Lean Planning Methodology</li>
        <li>Independent Schedule Quality Assessment</li>
        <li>Schedule Risk Analysis (Monte Carlo)</li>
        <li>Training</li>
      </ul>
    </div>

    <div class="group" style="top:264px">
      <span class="tag">Management of Risk<svg width="18" height="24" viewBox="0 0 18 24"><path d="M0,0 L8,0 L16,12 L8,24 L0,24 L8,12 Z" fill="#1a8ad8"/></svg></span>
      <ul class="list">
        <li>Risk Management Policies &amp; Procedures</li>
        <li>Risk Management Strategy</li>
        <li>Risk Registers</li>
        <li>Risk Response and Communication</li>
        <li>Cost &amp; Schedule Risk Analysis (Monte Carlo)</li>
        <li>Risk Management Training</li>
      </ul>
    </div>

    <div class="group" style="top:464px">
      <span class="tag">Cost Control<svg width="18" height="24" viewBox="0 0 18 24"><path d="M0,0 L8,0 L16,12 L8,24 L0,24 L8,12 Z" fill="#1a8ad8"/></svg></span>
      <ul class="list">
        <li>Estimating &amp; Forecasting</li>
        <li>Earned Value Management</li>
        <li>Progress Reporting</li>
        <li>Cost Risk Analysis (Monte Carlo)</li>
      </ul>
    </div>
  </div>

  <svg class="footer" width="849" height="138" viewBox="0 0 849 138">
    <defs>
      <linearGradient id="footGrad" x1="0" y1="0" x2="1" y2="0">
        <stop offset="0" stop-color="#1b3a8c"/>
        <stop offset=".6" stop-color="#1d3f95"/>
        <stop offset="1" stop-color="#15246a"/>
      </linearGradient>
    </defs>
    <path d="M0,22 C250,-6 560,10 849,80 L849,138 L0,138 Z" fill="#1b2f7a"/>
    <path d="M0,36 C260,8 560,30 849,98 L849,138 L0,138 Z" fill="url(#footGrad)"/>
    <path d="M300,12 C520,14 700,50 849,92" fill="none" stroke="#7cc2ee" stroke-width="3" opacity=".8"/>
  </svg>

  <ul class="contact">
    <li><svg width="16" height="12" viewBox="0 0 16 12"><rect x=".5" y=".5" width="15" height="11" fill="none" stroke="#fff"/><path d="M.5,.5 L8,7 L15.5,.5" fill="none" stroke="#fff"/></svg>info@<b>CORVANESERVICES</b>.ie</li>
    <li><svg width="16" height="16" viewBox="0 0 16 16"><circle cx="8" cy="8" r="7" fill="none" stroke="#fff"/><ellipse cx="8" cy="8" rx="3" ry="7" fill="none" stroke="#fff"/><path d="M1,8 H15 M2.5,4.5 H13.5 M2.5,11.5 H13.5" stroke="#fff"/></svg>www.<b>CORVANESERVICES</b>.ie</li>
    <li><svg width="16" height="16" viewBox="0 0 16 16"><path d="M3,1 L6,4 L4.5,6 C5.5,8 8,10.5 10,11.5 L12,10 L15,13 L13,15 C7,15 1,9 1,3 Z" fill="#fff"/></svg><b>+353 (0)870 555 014</b></li>
  </ul>

  <div class="foot-mark"></div>
</div>
</body>
</html>
```